Powerpoint Presentation design template

I am looking for a PPT presentation that show class and professionalism and in the same colour them as the logo. It should be simple, but yet classy and pro. The business is an oil and gas exploration and exploitation business. The business has nothing to do with solar panel and other renewable energies, so please no solar panel or wind farms in the background. It would be more oil rigs and LNG plant in the background of some slide templates...

oil and gas exploration and exploitation

```html
<!DOCTYPE html>
<html lang="en">
<head>
<meta charset="utf-8">
<title>Meridane Energy – Presentation Template</title>
<link rel="stylesheet" href="https://fonts.googleapis.com/css2?family=Poppins:wght@400;500;600;700&display=swap">
<style>
:root{
  --green:#8cc63f;
  --lime:#a6d84a;
  --blue:#29a9e0;
  --teal:#1fa39b;
  --ink:#151515;
  --grey:#6b6b6b;
  --line:#e4e4e4;
  --stage:#d9d9d9;
  --card:#ffffff;
}
*{margin:0;padding:0;box-sizing:border-box}
html,body{width:1200px;height:355px;overflow:hidden;background:var(--stage);font-family:'Poppins',sans-serif;color:var(--ink)}
.board{position:relative;width:1200px;height:355px}
.slide{position:absolute;width:292px;height:164px;background:#fff;overflow:hidden}
.r1{top:10px}.r2{top:181px}
.c1{left:7px}.c2{left:305px}.c3{left:603px}.c4{left:901px}
.abs{position:absolute}
.lorem{font-size:2.6px;line-height:1.55;color:var(--grey)}
.title{position:absolute;font-size:8px;font-weight:500;letter-spacing:.1px;white-space:nowrap}
.title b{font-weight:700}
.bar{position:absolute;height:1.3px;width:22px;background:var(--green)}
.footer{position:absolute;left:0;right:0;bottom:4px;height:8px;font-size:2.4px;color:var(--blue)}
.footer .sec{position:absolute;left:4px;bottom:1px}
.footer .pg{position:absolute;right:5px;bottom:1px}
.footer .brand{position:absolute;left:50%;transform:translateX(-50%);bottom:0;font-size:3.6px;font-weight:700;color:var(--teal);display:flex;align-items:center;gap:1.5px;white-space:nowrap}
.dot{display:inline-block;border-radius:50%;background:var(--teal)}
.photo{position:absolute}

/* cover */
.cover .photo{left:0;top:0;width:292px;height:152px;background:linear-gradient(180deg,#2c2a26 0%,#3b3227 45%,#1a1a1a 100%)}
.cover .copy{position:absolute;left:0;right:0;bottom:0;height:12px;background:#ececec;font-size:3.8px;text-align:center;line-height:12px;color:#333}
.cover .name{position:absolute;left:0;right:0;top:58px;text-align:center;color:var(--blue);font-weight:700;font-size:10px;line-height:1}
.cover .name small{display:block;font-size:5px;letter-spacing:2.4px;color:var(--blue);font-weight:500;margin-top:1px}
.cover .welcome{position:absolute;left:0;right:0;top:84px;text-align:center;color:#fff;font-size:7.5px}
.cover .big{position:absolute;left:0;right:0;top:94px;text-align:center;color:#fff;font-size:13px;font-weight:500;white-space:nowrap}
.cover .big span{color:var(--lime);font-weight:700}

/* agenda */
.agenda .panel{position:absolute;left:0;top:0;width:76px;height:164px;background:linear-gradient(160deg,#b7e063,#8cc63f)}
.agenda .photo{left:76px;top:0;width:89px;height:164px;background:linear-gradient(180deg,#5e89b2 0%,#9a8a72 40%,#5d5a55 70%,#3b3d42 100%)}
.agenda .name{position:absolute;left:0;width:76px;top:65px;text-align:center;color:var(--teal);font-weight:700;font-size:8.5px;line-height:1}
.agenda .name small{display:block;font-size:4.3px;letter-spacing:1.8px;font-weight:500}
.agenda .head{position:absolute;left:0;width:76px;top:100px;text-align:center;color:#fff;font-weight:700;font-size:10.5px}
.agenda ul{list-style:none;position:absolute;left:165px;top:7px;width:118px}
.agenda li{position:relative;height:21px;display:flex;align-items:center;font-size:5px;font-weight:500;padding-left:27px}
.agenda li::after{content:"";position:absolute;left:26px;right:0;bottom:0;height:.5px;background:var(--line)}
.agenda li svg{position:absolute;left:0;top:3px}

/* about */
.ring-photo{position:absolute;border-radius:50%}
.about ul{list-style:none;position:absolute;left:131px;top:35px;width:150px}
.about li{position:relative;padding-left:5px;margin-bottom:4.2px}
.about li::before{content:"";position:absolute;left:0;top:1px;width:2.4px;height:2.4px;border-radius:50%;border:.5px solid var(--green)}
.about li.sub{padding-left:9px;margin-bottom:.8px;font-size:2.4px}
.about li.sub::before{left:4px;border:none;border-radius:0;width:2px;height:2px;background:none;border-right:.6px solid var(--green);border-top:.6px solid var(--green);transform:rotate(45deg)}

/* expertise */
.exp-card{position:absolute;width:69px;height:50px;background:var(--card);box-shadow:0 0 3px rgba(0,0,0,.12);text-align:center;padding:4px 5px 0}
.exp-card h4{font-size:3.9px;font-weight:500;margin:2px 0 2px;white-space:nowrap}
.exp-card .ico{width:11px;height:11px;margin:0 auto;border:.6px solid var(--teal);border-radius:50%}

/* industry */
.map{position:absolute;left:7px;top:43px;width:136px;height:88px;border-radius:8px;background:radial-gradient(ellipse at 40% 50%,#35b3a6 0%,#7fc9d5 50%,#e6f4f7 100%)}
.pins{position:absolute;left:150px;top:38px;width:138px}
.pins::before{content:"";position:absolute;left:4.5px;top:6px;bottom:0;height:95px;width:.4px;background:#cfcfcf}
.pin{position:relative;height:20.6px;padding-left:15px}
.pin svg{position:absolute;left:0;top:1px}
.pin h5{font-size:3.7px;font-weight:500;color:var(--blue);line-height:1.2}

/* tech & team cards */
.tcard{position:absolute;width:65px;background:var(--card);box-shadow:0 0 3px rgba(0,0,0,.12);text-align:center}
.tech .tcard{top:40px;height:84px;padding:36px 4px 0}
.tech .tcard h4{font-size:4.2px;font-weight:500;color:var(--teal);line-height:1.5;height:13px;display:flex;align-items:center;justify-content:center;margin-bottom:3px}
.tcard .badge{position:absolute;left:50%;top:8px;transform:translateX(-50%);width:24px;height:24px;border-radius:50%;background:linear-gradient(180deg,transparent 50%,#1b1b1b 50%)}
.tcard .badge i{position:absolute;left:2px;top:1px;width:20px;height:20px;border-radius:50%;background:linear-gradient(160deg,#58c9bd,var(--teal));border:1.2px solid #fff}
.team .tcard{top:59px;height:77px;padding:24px 4px 0}
.team .avatar{position:absolute;left:50%;top:-20px;transform:translateX(-50%);width:38px;height:38px;border-radius:50%;border:1.2px solid var(--green);background:linear-gradient(180deg,#eef2f4,#c9d3da)}
.team h4{font-size:4.6px;font-weight:600}
.team .role{font-size:3.3px;color:var(--grey);margin-bottom:3px}
.team .lorem{color:#333}

/* contact */
.contact .deco{position:absolute;left:14px;top:20px;width:123px;height:121px;border-radius:50%;background:radial-gradient(circle at 40% 40%,#c9ecd0,#bfe3f3);display:flex;align-items:center;justify-content:center;font-size:10px;font-weight:700;color:var(--teal)}
.contact .name{position:absolute;left:156px;top:19px;font-size:10px;font-weight:700;color:var(--blue);line-height:1;display:flex;gap:3px;align-items:flex-start}
.contact .name small{display:block;font-size:5px;letter-spacing:2.4px;font-weight:500;text-align:right}
.contact .item{position:absolute;left:153px;display:flex;align-items:flex-start;gap:7px;font-size:4.8px;font-weight:500}
.contact .ic{width:11px;height:11px;background:#f1f1f1;display:flex;align-items:center;justify-content:center;flex:none}
</style>
</head>
<body>
<div class="board">

  <section class="slide r1 c1 cover">
    <div class="photo" role="img" aria-label="Offshore oil rig silhouetted at dusk over the sea"></div>
    <div class="name">MERIDANE<small>ENERGY</small></div>
    <div class="welcome">WELCOME TO</div>
    <div class="big"><span>MERIDANE</span> ENERGY</div>
    <div class="copy">© 2025 Meridane I All Rights Reserved</div>
  </section>

  <section class="slide r1 c2 agenda">
    <div class="panel"></div>
    <div class="name">MERIDANE<small>ENERGY</small></div>
    <div class="head">AGENDA</div>
    <div class="photo" role="img" aria-label="LNG processing plant with towers and pipework"></div>
    <ul>
      <li><svg width="21" height="15" viewBox="0 0 21 15"><rect x="0" y="0" width="14" height="15" fill="#29a9e0"/><circle cx="14" cy="7.5" r="7" fill="#29a9e0"/><circle cx="14" cy="7.5" r="4.8" fill="none" stroke="#fff" stroke-width=".7"/><path d="M13 5.3l2.2 2.2-2.2 2.2" fill="none" stroke="#fff" stroke-width=".8"/></svg>Introduction</li>
      <li><svg width="21" height="15" viewBox="0 0 21 15"><rect x="0" y="0" width="14" height="15" fill="#29a9e0"/><circle cx="14" cy="7.5" r="7" fill="#29a9e0"/><circle cx="14" cy="7.5" r="4.8" fill="none" stroke="#fff" stroke-width=".7"/><path d="M13 5.3l2.2 2.2-2.2 2.2" fill="none" stroke="#fff" stroke-width=".8"/></svg>About us</li>
      <li><svg width="21" height="15" viewBox="0 0 21 15"><rect x="0" y="0" width="14" height="15" fill="#29a9e0"/><circle cx="14" cy="7.5" r="7" fill="#29a9e0"/><circle cx="14" cy="7.5" r="4.8" fill="none" stroke="#fff" stroke-width=".7"/><path d="M13 5.3l2.2 2.2-2.2 2.2" fill="none" stroke="#fff" stroke-width=".8"/></svg>Our Expertise</li>
      <li><svg width="21" height="15" viewBox="0 0 21 15"><rect x="0" y="0" width="14" height="15" fill="#29a9e0"/><circle cx="14" cy="7.5" r="7" fill="#29a9e0"/><circle cx="14" cy="7.5" r="4.8" fill="none" stroke="#fff" stroke-width=".7"/><path d="M13 5.3l2.2 2.2-2.2 2.2" fill="none" stroke="#fff" stroke-width=".8"/></svg>Industry Presence</li>
      <li><svg width="21" height="15" viewBox="0 0 21 15"><rect x="0" y="0" width="14" height="15" fill="#29a9e0"/><circle cx="14" cy="7.5" r="7" fill="#29a9e0"/><circle cx="14" cy="7.5" r="4.8" fill="none" stroke="#fff" stroke-width=".7"/><path d="M13 5.3l2.2 2.2-2.2 2.2" fill="none" stroke="#fff" stroke-width=".8"/></svg>Technology &amp; Innovation</li>
      <li><svg width="21" height="15" viewBox="0 0 21 15"><rect x="0" y="0" width="14" height="15" fill="#29a9e0"/><circle cx="14" cy="7.5" r="7" fill="#29a9e0"/><circle cx="14" cy="7.5" r="4.8" fill="none" stroke="#fff" stroke-width=".7"/><path d="M13 5.3l2.2 2.2-2.2 2.2" fill="none" stroke="#fff" stroke-width=".8"/></svg>Our Team</li>
      <li><svg width="21" height="15" viewBox="0 0 21 15"><rect x="0" y="0" width="14" height="15" fill="#29a9e0"/><circle cx="14" cy="7.5" r="7" fill="#29a9e0"/><circle cx="14" cy="7.5" r="4.8" fill="none" stroke="#fff" stroke-width=".7"/><path d="M13 5.3l2.2 2.2-2.2 2.2" fill="none" stroke="#fff" stroke-width=".8"/></svg>Contact Us</li>
    </ul>
  </section>

  <section class="slide r1 c3 about">
    <svg class="abs" style="left:5px;top:17px" width="124" height="124" viewBox="0 0 124 124"><path d="M62 4A58 58 0 0 0 12 92" fill="none" stroke="#8cc63f" stroke-width="3"/><path d="M84 8A58 58 0 0 1 36 114" fill="none" stroke="#29a9e0" stroke-width="5"/></svg>
    <div class="ring-photo" style="left:13px;top:25px;width:106px;height:106px;background:radial-gradient(circle at 55% 40%,#f8c24a,#e67a1c 55%,#5a2f10)" role="img" aria-label="Oil pump jack at sunset in a field"></div>
    <div class="bar" style="left:131px;top:15px"></div>
    <div class="title" style="left:131px;top:19px">ABOUT <b style="font-weight:500">US</b></div>
    <ul class="lorem">
      <li>Lorem ipsum is simply dummy text of the printing and typesetting industry. Lorem ipsum has been the industry's standard dummy text ever</li>
      <li>Lorem ipsum is simply dummy text of the printing and typesetting industry. Lorem ipsum has been the industry's standard dummy text ever</li>
      <li>Lorem ipsum is simply dummy text of the printing and typesetting industry. Lorem ipsum has been the industry's standard dummy text ever</li>
      <li>Lorem ipsum is simply dummy text of the printing and typesetting industry. Lorem ipsum has been the industry's standard dummy text ever</li>
      <li class="sub">Lorem ipsum is simply dummy text of the printing and typesetting industry.</li>
      <li class="sub">Lorem ipsum is simply dummy text of the printing and typesetting industry.</li>
      <li class="sub">Lorem ipsum is simply dummy text of the printing and typesetting industry.</li>
      <li class="sub">Lorem ipsum is simply dummy text of the printing and typesetting industry.</li>
    </ul>
    <div class="footer"><span class="sec">About Us</span><span class="brand"><i class="dot" style="width:4px;height:4px"></i>MERIDANE</span><span class="pg">Page No 3</span></div>
  </section>

  <section class="slide r1 c4 expertise">
    <div class="bar" style="left:9px;top:14px"></div>
    <div class="title" style="left:9px;top:18px">OUR <b>EXPERTISE</b></div>
    <div class="exp-card" style="left:11px;top:35px"><div class="ico"></div><h4>Exploration Technique</h4><p class="lorem">Lorem ipsum is simply dummy text of the printing and typesetting industry. Lorem</p></div>
    <div class="exp-card" style="left:87px;top:35px"><div class="ico"></div><h4>Drilling Operations</h4><p class="lorem">Lorem ipsum is simply dummy text of the printing and typesetting industry. Lorem</p></div>
    <div class="exp-card" style="left:11px;top:96px"><div class="ico"></div><h4>Production &amp; Refining</h4><p class="lorem">Lorem ipsum is simply dummy text of the printing and typesetting industry. Lorem</p></div>
    <div class="exp-card" style="left:87px;top:96px"><div class="ico"></div><h4>Investment &amp; Partnerships</h4><p class="lorem">Lorem ipsum is simply dummy text of the printing and typesetting industry. Lorem</p></div>
    <svg class="abs" style="left:165px;top:22px" width="118" height="118" viewBox="0 0 118 118"><path d="M59 3A56 56 0 0 0 8 82" fill="none" stroke="#8cc63f" stroke-width="3"/><path d="M84 9A56 56 0 0 1 30 110" fill="none" stroke="#29a9e0" stroke-width="5"/></svg>
    <div class="ring-photo" style="left:172px;top:29px;width:104px;height:104px;background:linear-gradient(170deg,#6d7fa6,#b99a8a 45%,#3d4a5c 80%)" role="img" aria-label="Engineer in hard hat overlooking a refinery at dusk"></div>
    <div class="footer"><span class="sec">Our Expertise</span><span class="brand"><i class="dot" style="width:4px;height:4px"></i>MERIDANE</span><span class="pg">Page No 3</span></div>
  </section>

  <section class="slide r2 c1 industry">
    <div class="bar" style="left:134px;top:14px"></div>
    <div class="title" style="left:103px;top:18px"><b>INDUSTRY</b> PRESENCE</div>
    <div class="map" role="img" aria-label="Dotted world map in teal and green"></div>
    <div class="pins">
      <div class="pin"><svg width="10" height="10" viewBox="0 0 10 10"><circle cx="5" cy="5" r="4.6" fill="#fff" stroke="#8cc63f" stroke-width=".6"/><path d="M5 2.3a1.8 1.8 0 0 1 1.8 1.8C6.8 5.5 5 7.6 5 7.6S3.2 5.5 3.2 4.1A1.8 1.8 0 0 1 5 2.3z" fill="#1fa39b"/></svg><h5>Lorem Ipsum</h5><p class="lorem">Lorem ipsum is simply dummy text of the printing and typesetting industry. Lorem ipsum has been the industry's standard dummy text ever since the 1500s</p></div>
      <div class="pin"><svg width="10" height="10" viewBox="0 0 10 10"><circle cx="5" cy="5" r="4.6" fill="#fff" stroke="#8cc63f" stroke-width=".6"/><path d="M5 2.3a1.8 1.8 0 0 1 1.8 1.8C6.8 5.5 5 7.6 5 7.6S3.2 5.5 3.2 4.1A1.8 1.8 0 0 1 5 2.3z" fill="#1fa39b"/></svg><h5>Lorem Ipsum</h5><p class="lorem">Lorem ipsum is simply dummy text of the printing and typesetting industry. Lorem ipsum has been the industry's standard dummy text ever since the 1500s</p></div>
      <div class="pin"><svg width="10" height="10" viewBox="0 0 10 10"><circle cx="5" cy="5" r="4.6" fill="#fff" stroke="#8cc63f" stroke-width=".6"/><path d="M5 2.3a1.8 1.8 0 0 1 1.8 1.8C6.8 5.5 5 7.6 5 7.6S3.2 5.5 3.2 4.1A1.8 1.8 0 0 1 5 2.3z" fill="#1fa39b"/></svg><h5>Lorem Ipsum</h5><p class="lorem">Lorem ipsum is simply dummy text of the printing and typesetting industry. Lorem ipsum has been the industry's standard dummy text ever since the 1500s</p></div>
      <div class="pin"><svg width="10" height="10" viewBox="0 0 10 10"><circle cx="5" cy="5" r="4.6" fill="#fff" stroke="#8cc63f" stroke-width=".6"/><path d="M5 2.3a1.8 1.8 0 0 1 1.8 1.8C6.8 5.5 5 7.6 5 7.6S3.2 5.5 3.2 4.1A1.8 1.8 0 0 1 5 2.3z" fill="#1fa39b"/></svg><h5>Lorem Ipsum</h5><p class="lorem">Lorem ipsum is simply dummy text of the printing and typesetting industry. Lorem ipsum has been the industry's standard dummy text ever since the 1500s</p></div>
      <div class="pin"><svg width="10" height="10" viewBox="0 0 10 10"><circle cx="5" cy="5" r="4.6" fill="#fff" stroke="#8cc63f" stroke-width=".6"/><path d="M5 2.3a1.8 1.8 0 0 1 1.8 1.8C6.8 5.5 5 7.6 5 7.6S3.2 5.5 3.2 4.1A1.8 1.8 0 0 1 5 2.3z" fill="#1fa39b"/></svg><h5>Lorem Ipsum</h5><p class="lorem">Lorem ipsum is simply dummy text of the printing and typesetting industry. Lorem ipsum has been the industry's standard dummy text ever since the 1500s</p></div>
    </div>
    <div class="footer"><span class="sec">Industry Presence</span><span class="brand"><i class="dot" style="width:4px;height:4px"></i>MERIDANE</span><span class="pg">Page No 5</span></div>
  </section>

  <section class="slide r2 c2 tech">
    <div class="bar" style="left:136px;top:15px"></div>
    <div class="title" style="left:85px;top:19px"><b>TECHNOLOGY &amp;</b> INNOVATION</div>
    <div class="tcard" style="left:8px"><div class="badge"><i></i></div><h4>Advanced Seismic Data Analysis</h4><p class="lorem">Lorem ipsum is simply dummy text of the printing and typesetting industry. Lorem ipsum has been the industry's standard dummy text ever</p></div>
    <div class="tcard" style="left:79px"><div class="badge"><i></i></div><h4>Enhanced Oil Recovery (EOR)</h4><p class="lorem">Lorem ipsum is simply dummy text of the printing and typesetting industry. Lorem ipsum has been the industry's standard dummy text ever</p></div>
    <div class="tcard" style="left:149px"><div class="badge"><i></i></div><h4>LNG Production &amp; Processing</h4><p class="lorem">Lorem ipsum is simply dummy text of the printing and typesetting industry. Lorem ipsum has been the industry's standard dummy text ever</p></div>
    <div class="tcard" style="left:219px"><div class="badge"><i></i></div><h4>Safety Innovations</h4><p class="lorem">Lorem ipsum is simply dummy text of the printing and typesetting industry. Lorem ipsum has been the industry's standard dummy text ever</p></div>
    <div class="footer"><span class="sec">Technology &amp; Innovation</span><span class="brand"><i class="dot" style="width:4px;height:4px"></i>MERIDANE</span><span class="pg">Page No 6</span></div>
  </section>

  <section class="slide r2 c3 team">
    <div class="bar" style="left:134px;top:15px"></div>
    <div class="title" style="left:123px;top:19px">OUR <b style="font-weight:500">TEAM</b></div>
    <div class="tcard" style="left:8px"><div class="avatar" role="img" aria-label="Portrait photo of team member"></div><h4>Liam</h4><p class="role">Co-Founder</p><p class="lorem">Lorem ipsum is simply dummy text of the printing and typesetting industry. Lorem ipsum has been the industry's</p></div>
    <div class="tcard" style="left:78px"><div class="avatar" role="img" aria-label="Portrait photo of team member"></div><h4>Nathan</h4><p class="role">CEO, &amp; Co-Founder</p><p class="lorem">Lorem ipsum is simply dummy text of the printing and typesetting industry. Lorem ipsum has been the industry's</p></div>
    <div class="tcard" style="left:148px"><div class="avatar" role="img" aria-label="Portrait photo of team member"></div><h4>Elias</h4><p class="role">Chairman</p><p class="lorem">Lorem ipsum is simply dummy text of the printing and typesetting industry. Lorem ipsum has been the industry's</p></div>
    <div class="tcard" style="left:218px"><div class="avatar" role="img" aria-label="Portrait photo of team member"></div><h4>Owen Clarke</h4><p class="role">Support</p><p class="lorem">Lorem ipsum is simply dummy text of the printing and typesetting industry. Lorem ipsum has been the industry's</p></div>
    <div class="footer"><span class="sec">Our Team</span><span class="brand"><i class="dot" style="width:4px;height:4px"></i>MERIDANE</span><span class="pg">Page No 7</span></div>
  </section>

  <section class="slide r2 c4 contact">
    <div class="deco">MERIDANE</div>
    <div class="name"><div>MERIDANE<small>ENERGY</small></div></div>
    <div class="bar" style="left:153px;top:47px"></div>
    <div class="title" style="left:153px;top:52px"><b>CONTACT</b> US</div>
    <div class="item" style="top:76px"><span class="ic"><svg width="7" height="7" viewBox="0 0 24 24"><path d="M6.6 10.8a15 15 0 0 0 6.6 6.6l2.2-2.2a1 1 0 0 1 1-.25 11.4 11.4 0 0 0 3.6.57 1 1 0 0 1 1 1V20a1 1 0 0 1-1 1A17 17 0 0 1 3 4a1 1 0 0 1 1-1h3.5a1 1 0 0 1 1 1c0 1.25.2 2.45.57 3.6a1 1 0 0 1-.25 1z" fill="#1fa39b"/></svg></span><span style="padding-top:2.5px">+1 555 010 2040</span></div>
    <div class="item" style="top:96px"><span class="ic"><svg width="7" height="6" viewBox="0 0 24 18"><rect x="1" y="1" width="22" height="16" rx="2" fill="#1fa39b"/><path d="M2 2l10 8 10-8" fill="none" stroke="#fff" stroke-width="1.8"/></svg></span><span style="padding-top:2.5px">admin@meridane.com</span></div>
    <div class="item" style="top:113px"><span class="ic"><svg width="6" height="8" viewBox="0 0 16 22"><path d="M8 1a7 7 0 0 1 7 7c0 5-7 13-7 13S1 13 1 8a7 7 0 0 1 7-7z" fill="none" stroke="#1fa39b" stroke-width="2"/><circle cx="8" cy="8" r="2.5" fill="#1fa39b"/></svg></span><span style="padding-top:1px;line-height:1.9">20 Meridane, Lorem Ipsum<br>Lorem Ipsum</span></div>
    <div class="footer"><span class="brand"><i class="dot" style="width:4px;height:4px"></i>MERIDANE</span></div>
  </section>

</div>
</body>
</html>
```